Charity website needing new website design

Hi there. We are looking to get a revamped website for our non for profit charity. We specialise in eye cataract surgeries and ear care around the world. Please visit our website brightpathrelief.org.au for the current layout.
I have attached a brief with photos. The about us page please include an interactive map showing our locations we operate in. The website should be easy to use, match our logo design and be clear to navigate. Pixelvault and other images can be used if they fit the scheme of the website and feel. The donation page should incorporate the gateway to receive donations. The team page should have each photo of the team member next to it. Please compare to other charity websites such as KORAMEN, Globe Harbor etc. Another website which has a lovely and easy to use scheme is tlnqaustralia.org.au
The tabs should be in the following order:
About us, Why Health? Our Team, Eye Care Programs, Ear Care Programs, Contact Us, Donate.
Please make sure the website is both compatible with mobile & computer.
The Registered Charity Logo can be at the footer of the page with details of brightpath etc

```html
<!DOCTYPE html>
<html lang="en">
<head>
<meta charset="utf-8">
<title>Brightpath Aid Foundation</title>
<link rel="stylesheet" href="https://fonts.googleapis.com/css2?family=Teko:wght@500;600&family=Montserrat:wght@400;500;600;700&display=swap">
<style>
:root{
  --green:#3cb56a;
  --green-dark:#2e9c57;
  --orange:#f4a42a;
  --navy:#0f4a63;
  --footer:#143b4c;
  --sand:#f3f2ee;
  --ink:#2a3a44;
  --muted:#4a5560;
  --white:#ffffff;
  --canvas:#e9e9e7;
}
*{box-sizing:border-box;margin:0;padding:0}
html,body{width:1200px;height:3834px;overflow:hidden;background:var(--canvas)}
body{font-family:"Montserrat",sans-serif;color:var(--ink)}
.page{position:absolute;left:0;top:75px;width:1200px;height:3684px;background:var(--white);overflow:hidden}
.abs{position:absolute}
.heading{font-family:"Teko",sans-serif;font-weight:600;text-transform:uppercase;letter-spacing:.5px;line-height:1}
.btn{position:absolute;display:flex;align-items:center;justify-content:center;font-size:9px;font-weight:600;color:var(--white);text-transform:uppercase;letter-spacing:.3px;border-radius:2px}
.btn-green{background:var(--green)}
.btn-orange{background:var(--orange)}
.rule::after{content:"";display:inline-block;width:16px;height:1.5px;background:currentColor;margin-left:8px;vertical-align:middle;opacity:.6}
.rule-both::before{content:"";display:inline-block;width:16px;height:1.5px;background:currentColor;margin-right:8px;vertical-align:middle;opacity:.6}
p{font-size:10.5px;line-height:1.55;color:var(--muted)}

/* header */
.site-header{left:0;top:0;width:1200px;height:86px;background:var(--white)}
.brand{left:166px;top:10px;width:134px;height:70px;border-bottom:2px solid var(--navy);display:flex;flex-direction:column;align-items:center;justify-content:flex-end;padding-bottom:6px}
.brand-dot{width:26px;height:26px;border-radius:50%;background:var(--green);margin-bottom:6px}
.brand-name{font-size:13px;font-weight:700;color:var(--navy);letter-spacing:.5px;line-height:1}
.brand-sub{font-size:7px;font-weight:600;color:var(--navy);letter-spacing:1.5px}
.social{width:14px;height:14px;border-radius:2px}
.social-a{background:var(--orange)}
.social-b{background:var(--navy)}
.nav{left:467px;top:40px;display:flex;gap:18px;font-size:10px;font-weight:500;color:var(--navy)}
.nav .active{color:var(--orange)}

/* hero */
.hero{left:0;top:86px;width:1200px;height:611px}
.hero-photo{position:absolute;inset:0;background:linear-gradient(100deg,#14404a 0%,#2a5d63 40%,#4e7f86 70%,#9fb9c4 100%)}
.hero h1{position:absolute;left:152px;top:164px;font-size:40px;color:var(--white);line-height:.95;letter-spacing:1px}
.hero h1 .hl{color:var(--orange)}
.hero p{position:absolute;left:152px;top:296px;width:420px;color:#e6eef0;font-size:11px}

/* about */
.about-mark{left:200px;top:790px;width:360px;height:270px}
.about h2{position:absolute;left:642px;top:775px;font-size:30px;color:var(--navy)}

/* why */
.why{left:0;top:1144px;width:644px;height:497px;background:var(--navy)}
.why-photo{left:644px;top:1144px;width:556px;height:497px;background:linear-gradient(135deg,#7a4a30 0%,#b89c85 40%,#d8d2c8 65%,#8f7a60 100%)}
.sand{left:0;top:1641px;width:1200px;height:775px;background:var(--sand)}

/* facts */
.facts{left:181px;top:1577px;width:840px;height:322px;background:var(--white);box-shadow:0 4px 18px rgba(0,0,0,.06)}
.fact{position:absolute;top:118px;width:190px}
.fact .num{font-size:14px;font-weight:700;color:var(--orange);margin-bottom:4px}
.fact p{font-size:9.5px;line-height:1.3;color:var(--ink)}
.fact-sep{position:absolute;top:118px;width:1px;height:105px;background:#dcdcdc}

/* team */
.member{position:absolute;top:2028px;width:206px;height:246px;overflow:hidden}
.member .photo{position:absolute;inset:0}
.member .info{position:absolute;left:15px;bottom:16px;right:12px;color:var(--white)}
.member .name{font-size:11px;font-weight:700;color:var(--orange);text-transform:uppercase;line-height:1.15}
.member .role{font-size:9px;font-weight:600}
.member .cred{font-size:8px;opacity:.85}
.member .stripe{position:absolute;left:0;bottom:0;width:100%;height:4px;background:var(--green)}

/* programs */
.prog-photo{top:2419px;width:600px;height:411px}
.prog-box{top:2673px;width:449px;height:188px;background:var(--navy);text-align:center}
.prog-box h3{font-size:29px;color:var(--green);margin-top:26px}
.prog-box p{color:#d5e2e8;width:380px;margin:8px auto 0;font-size:9.5px;line-height:1.45}

/* newsletter */
.news-art{left:247px;top:2959px;width:223px;height:179px;border-radius:6px;background:radial-gradient(circle at 55% 55%,#f3c46e 0%,#e9ecf2 60%,#ffffff 100%)}
.news h2{position:absolute;left:538px;top:2936px;font-size:31px;color:var(--navy)}
.label{position:absolute;font-size:8.5px;font-weight:600;color:var(--ink)}
.input{position:absolute;height:31px;border:1px solid #d8d8d8;border-radius:2px;font-size:8px;color:#b0b0b0;padding:11px 10px}

/* footer */
.footer{left:0;top:3254px;width:1200px;height:430px}
.footer h4{position:absolute;font-size:19px;color:var(--orange)}
.footer .item{position:absolute;font-size:10px;color:#dfe8ec;display:flex;align-items:center;gap:8px}
.quick a{position:absolute;font-size:10px;color:#dfe8ec;text-decoration:none}
.footer-brand{left:152px;top:170px;width:163px;height:120px;display:flex;flex-direction:column;align-items:center;justify-content:flex-end}
.footer-brand .brand-name{color:var(--white);font-size:17px}
.footer-brand .brand-sub{color:var(--white);font-size:9px;border-top:1px solid #fff;padding-top:2px}
.bottom-bar{left:0;top:402px;width:1200px;height:28px;background:var(--green)}
</style>
</head>
<body>
<div class="page">

  <!-- header -->
  <header class="site-header abs">
    <div class="brand abs"><span class="brand-dot"></span><span class="brand-name">BRIGHTPATH AID</span><span class="brand-sub">FOUNDATION</span></div>
    <span class="social social-a abs" style="left:821px;top:16px"></span>
    <span class="social social-b abs" style="left:847px;top:16px;width:10px;height:10px;top:18px"></span>
    <span class="btn btn-green" style="left:881px;top:12px;width:93px;height:25px">Donate now</span>
    <nav class="nav abs" aria-label="Main">
      <span class="active">Home</span><span>About Us</span><span>Why Health?</span><span>Our Team</span><span>Eye Care Programs</span><span>Ear Care Programs</span><span>Contact Us</span>
    </nav>
  </header>

  <!-- hero -->
  <section class="hero abs">
    <div class="hero-photo" role="img" aria-label="Photo of a nurse in a blue cap and mask examining a child's eyes"></div>
    <h1 class="heading"><span class="hl">Help bring basic</span><br>health care <span class="hl">to every</span><br><span class="hl">person on the planet.</span></h1>
    <p>Through symbiotic health programs brightpath aid foundation provides innovative solutions to Eye and Hearing Health in the developing world with an ethical professional and sustainable approach.</p>
    <span class="btn btn-green" style="left:152px;top:372px;width:100px;height:27px">Read more</span>
    <svg class="abs" style="left:0;top:531px" width="1200" height="80" viewBox="0 0 1200 80" aria-hidden="true">
      <path d="M0 34 C180 12 420 10 600 62 C780 10 1020 12 1200 34 L1200 80 L0 80 Z" fill="var(--green)"/>
      <path d="M0 46 C180 24 420 22 600 78 C780 22 1020 24 1200 46 L1200 80 L0 80 Z" fill="var(--white)"/>
    </svg>
  </section>

  <!-- about -->
  <section class="about">
    <div class="about-mark abs" aria-label="Brightpath Aid Foundation">
      <span class="abs" style="left:10px;top:110px;font-size:22px;font-weight:700;color:var(--navy)">BRIGHTPATH AID</span>
      <span class="abs" style="left:240px;top:140px;width:96px;height:96px;border-radius:50%;background:var(--white);border:6px solid var(--navy)"></span>
    </div>
    <h2 class="heading rule">About us</h2>
    <p class="abs" style="left:642px;top:826px;width:385px">Brightpath Aid Foundation is dedicated to improving and transforming the lives of people through enhanced vision and hearing health in the developing world. Our mission is to bridge the gap in access to essential eye and hearing care, ensuring that everyone, regardless of their circumstances, has the opportunity to see and hear clearly.</p>
    <p class="abs" style="left:642px;top:942px;width:385px">With over 70 years of humanitarian aid across our members, we are passionate to provide innovative, sustainable, ethical and professional symbiotic solutions across multiple health...</p>
    <span class="btn btn-green" style="left:642px;top:1030px;width:100px;height:25px">Read more</span>
    <span class="btn btn-orange" style="left:751px;top:1030px;width:112px;height:25px">Donate now</span>
  </section>

  <!-- why health -->
  <div class="sand abs"></div>
  <section class="why abs">
    <h2 class="heading rule abs" style="left:152px;top:74px;font-size:30px;color:var(--green)">Why health?</h2>
    <p class="abs" style="left:152px;top:124px;width:415px;color:#d3e0e6">Charities often focus on the last component of aid, which is at times critically required without focusing on the root cause of poverty. Brightpath Aid Foundation focuses on the fundamental factors of poverty through providing health programs such as preventable blindness operations and hearing loss restoration.</p>
    <p class="abs" style="left:152px;top:226px;width:415px;color:#d3e0e6">Our approach is to establish mobile eye clinics in needing communities around the world. These communities are pinpointed by our on the ground contacts &amp; medical practitioners that have done extensive research to locate people in demand of health assistance.</p>
    <span class="btn btn-orange" style="left:152px;top:329px;width:83px;height:25px">Read more</span>
    <span class="btn btn-green" style="left:243px;top:329px;width:102px;height:25px">Donate now</span>
  </section>
  <div class="why-photo abs" role="img" aria-label="Photo of a doctor examining an elderly man's eyes at a mobile clinic"></div>

  <!-- did you know -->
  <section class="facts abs">
    <h2 class="heading rule rule-both abs" style="left:0;width:840px;top:52px;text-align:center;font-size:30px;color:var(--navy)">Did you know?</h2>
    <div class="fact" style="left:48px"><div class="num">$410.7 BILLION</div><p>loss in productivity occurs in the world due to sight loss. Restoring sight loss will create positive change and restores life.</p></div>
    <span class="fact-sep" style="left:255px"></span>
    <div class="fact" style="left:270px;width:175px"><div class="num">2 BILLION</div><p>people drink annually from a contaminated water source leading to half a million diarrheal deaths. Improving quality water systems will prevent death and diseases</p></div>
    <span class="fact-sep" style="left:505px"></span>
    <div class="fact" style="left:534px;width:240px"><div class="num">430 MILLION</div><p>people have disability level hearing loss in low and middle income countries. Establishing cochlear implant and hearing aid clinics will help people hear their loved ones again and are less dependent on daily community assistance.</p></div>
    <span class="btn btn-green" style="left:364px;top:243px;width:111px;height:27px">Donate now</span>
  </section>

  <!-- team -->
  <h2 class="heading rule rule-both abs" style="left:0;width:1200px;top:1970px;text-align:center;font-size:30px;color:var(--green)">Our team</h2>
  <div class="member" style="left:152px">
    <div class="photo" role="img" aria-label="Portrait of a team member in a dark suit" style="background:linear-gradient(180deg,#d9d6d2 0%,#8a7b70 60%,#2c2a2c 100%)"></div>
    <div class="info"><div class="name">Daniel Reyes</div><div class="role">Marketing Manager</div><div class="cred">APIA AFA Bcom Acc IP</div></div>
    <span class="stripe"></span>
  </div>
  <div class="member" style="left:383px">
    <div class="photo" role="img" aria-label="Portrait of a team member with long dark hair" style="background:linear-gradient(180deg,#ece9e6 0%,#a08677 55%,#3a2b28 100%)"></div>
    <div class="info"><div class="name">Leila Moreau</div><div class="role">Volunteer</div><div class="cred">Dip. ASCA, Dip. Comm. ASCA, Cert...</div></div>
    <span class="stripe"></span>
  </div>
  <div class="member" style="left:613px">
    <div class="photo" role="img" aria-label="Portrait of the founding member" style="background:linear-gradient(180deg,#8c8c8c 0%,#4d4b4a 50%,#1e2024 100%)"></div>
    <div class="info" style="bottom:30px"><div class="name">Omar Castell</div><div class="role">Founding member &amp; Patron</div><div class="cred">FCPA, FCCA, CTA, JP</div><div class="cred" style="margin-top:6px;line-height:1.35">Omar Castell is the founding member and patron of Brightpath Aid Foundation. Historically serving on various not-for-profit...</div></div>
    <span class="abs" style="left:15px;top:207px;width:17px;height:14px;background:var(--orange);border-radius:2px"></span>
    <svg class="abs" style="left:19px;top:210px" width="9" height="8" viewBox="0 0 9 8" aria-hidden="true"><path d="M0 4H8M5 1L8 4L5 7" stroke="#fff" stroke-width="1.3" fill="none"/></svg>
    <span class="stripe" style="background:var(--orange)"></span>
  </div>
  <div class="member" style="left:844px">
    <div class="photo" role="img" aria-label="Portrait of a founding member outdoors" style="background:linear-gradient(180deg,#e4e6e4 0%,#b6aea2 55%,#4a4a48 100%)"></div>
    <div class="info"><div class="name">Karim<br>Valdoro</div><div class="role">Founding member</div><div class="cred">MBA, M.Eng, ITIL, SNIA CA</div></div>
    <span class="stripe"></span>
  </div>
  <span class="btn btn-green" style="left:555px;top:2317px;width:90px;height:25px">View all</span>

  <!-- programs -->
  <div class="prog-photo abs" style="left:0" role="img" aria-label="Photo of a woman having an eye examination at a slit lamp" style="background:#999"></div>
  <div class="prog-photo abs" style="left:0;background:linear-gradient(120deg,#cbc6c0 0%,#a89a8e 40%,#3e3f45 75%,#d9dad8 100%)"></div>
  <div class="prog-photo abs" style="left:600px;background:linear-gradient(120deg,#9db0c0 0%,#c8ccd2 40%,#5a4d48 70%,#8c8580 100%)" role="img" aria-label="Photo of a doctor examining a patient's ear"></div>
  <section class="prog-box abs" style="left:152px">
    <h3 class="heading">Eye care programs</h3>
    <p>We all need our eyes to see and to complete our daily activities with ease. Imagine losing your eyesight, becoming dependent on family and friends for help and support to complete even the basic of activities...</p>
    <span class="btn btn-green" style="left:111px;top:127px;width:100px;height:27px">Read more</span>
    <span class="btn btn-orange" style="left:219px;top:127px;width:111px;height:27px">Donate now</span>
  </section>
  <section class="prog-box abs" style="left:600px">
    <h3 class="heading">Ear care programs</h3>
    <p>Hearing is a vital sense and gives us the ability to communicate with others in a way that none of our other senses can achieve. The loss of hearing can have a negative impact both on individuals...</p>
    <span class="btn btn-green" style="left:111px;top:127px;width:100px;height:27px">Read more</span>
    <span class="btn btn-green" style="left:219px;top:127px;width:111px;height:27px">Donate now</span>
  </section>

  <!-- newsletter -->
  <section class="news">
    <div class="news-art abs" role="img" aria-label="Illustration of an open envelope with a letter and a paper plane"></div>
    <h2 class="heading rule">Sign up to our newsletter</h2>
    <p class="abs" style="left:538px;top:2978px;width:380px;font-size:9px;line-height:1.45;color:var(--ink)">Thank you for your interest in Brightpath Aid Foundation. Please feel free to reach out to us using the information below or send us a message in the box provided.</p>
    <span class="label" style="left:538px;top:3018px">Name</span>
    <span class="label" style="left:751px;top:3018px">Email</span>
    <div class="input" style="left:538px;top:3033px;width:201px">Type here</div>
    <div class="input" style="left:751px;top:3033px;width:199px">Type here</div>
    <span class="label" style="left:538px;top:3082px">Subject</span>
    <div class="input" style="left:538px;top:3098px;width:412px">Type here</div>
    <span class="btn btn-green" style="left:538px;top:3150px;width:92px;height:29px">Submit</span>
  </section>

  <!-- footer -->
  <footer class="footer abs">
    <svg class="abs" style="left:0;top:0" width="1200" height="402" viewBox="0 0 1200 402" aria-hidden="true">
      <path d="M0 32 C220 32 430 40 600 0 C770 40 980 32 1200 32 L1200 402 L0 402 Z" fill="var(--green)"/>
      <path d="M0 44 C220 44 430 52 600 14 C770 52 980 44 1200 44 L1200 402 L0 402 Z" fill="var(--footer)"/>
    </svg>
    <div class="footer-brand abs"><span class="brand-dot" style="width:34px;height:34px;background:var(--white);margin-bottom:14px"></span><span class="brand-name">BRIGHTPATH AID</span><span class="brand-sub">FOUNDATION</span></div>

    <h4 class="heading rule" style="left:384px;top:168px">Contact us</h4>
    <div class="item" style="left:384px;top:204px"><svg width="9" height="9" viewBox="0 0 10 10"><path d="M2 1l2 2-1 1.5c.8 1.4 1.6 2.2 3 3L7.5 6 9.5 8 8 9.5C4 9 1 6 .5 2Z" fill="var(--green)"/></svg>0061-29048817362</div>
    <div class="item" style="left:384px;top:232px"><svg width="10" height="8" viewBox="0 0 10 8"><rect x=".5" y=".5" width="9" height="7" fill="none" stroke="var(--green)"/><path d="M.5 .5L5 4.5 9.5.5" fill="none" stroke="var(--green)"/></svg>info@brightpathrelief.org.au</div>
    <div class="item" style="left:384px;top:260px"><svg width="8" height="11" viewBox="0 0 8 11"><path d="M4 11S0 6 0 4a4 4 0 0 1 8 0c0 2-4 7-4 7Z" fill="var(--green)"/><circle cx="4" cy="4" r="1.5" fill="var(--footer)"/></svg>Brightpath Aid Foundation</div>
    <div class="item heading" style="left:384px;top:296px;font-size:15px;color:var(--orange)">ABN: <span style="color:#fff;margin-left:4px">47 210 386 591</span></div>

    <h4 class="heading rule" style="left:622px;top:168px">Quick link</h4>
    <nav class="quick" aria-label="Footer">
      <a style="left:622px;top:207px;color:var(--orange);text-decoration:underline">Home</a>
      <a style="left:622px;top:228px">About Us</a>
      <a style="left:622px;top:249px">Why Health?</a>
      <a style="left:622px;top:270px">Our Team</a>
      <a style="left:622px;top:291px">Eye Care Programs</a>
      <a style="left:622px;top:312px">Ear Care Programs</a>
      <a style="left:622px;top:333px">Contact Us</a>
    </nav>

    <h4 class="heading rule" style="left:806px;top:168px">Bank details</h4>
    <p class="abs" style="left:806px;top:205px;width:210px;color:#dfe8ec;font-size:10px;line-height:1.4">Lorem Ipsum is simply dummy text of the printing industry.</p>
    <div class="input" style="left:806px;top:243px;width:243px;background:#fff;border:none">Type here</div>
    <span class="btn btn-green" style="left:806px;top:288px;width:93px;height:27px">Subscribe</span>

    <div class="bottom-bar abs">
      <span class="abs" style="left:152px;top:8px;font-size:9px;color:#fff">© 2024 Brightpath. all right reserved</span>
      <span class="social social-a abs" style="left:1001px;top:7px"></span>
      <span class="social abs" style="left:1032px;top:9px;width:10px;height:10px;background:var(--white)"></span>
    </div>
  </footer>

</div>
</body>
</html>
```